International service dog training school needs web design

We need to upgrade our website. The website is https://brevantmoor.example/
We help trainers and service dog programs learn how to train service dogs with the latest and most ethical training methods. We offer online and in-person coaching services. We would like to see designs that are engaging and communicate professionalism, expertise, and care for the dogs and people we work with. Please also keep the colors already in the logo in the design.

```html
<!DOCTYPE html>
<html lang="en">
<head>
<meta charset="utf-8">
<title>Brevantmoor Center for Medical Assistance Canines</title>
<link href="https://fonts.googleapis.com/css2?family=Montserrat:wght@400;500;600;700&family=Varela+Round&display=swap" rel="stylesheet">
<style>
:root{
  --teal:#0aa39b;
  --blue:#1e73be;
  --ink:#222;
  --grey:#777;
  --light:#f3f3f3;
  --dark:#2b2b2b;
  --white:#fff;
}
*{box-sizing:border-box;margin:0;padding:0}
html,body{width:1200px;height:5133px;overflow:hidden}
body{position:relative;font-family:"Varela Round",sans-serif;color:var(--ink);background:var(--white)}
.abs{position:absolute}
.head{font-family:"Montserrat",sans-serif;font-weight:600;text-transform:uppercase;letter-spacing:.3px}
.btn{position:absolute;display:flex;align-items:center;justify-content:center;border-radius:24px;color:var(--white);font-family:"Montserrat",sans-serif;font-weight:700;font-size:13px;text-transform:uppercase;text-decoration:none}
.btn.teal{background:var(--teal)}
.btn.blue{background:var(--blue)}
.photo{position:absolute}
/* top bar */
.topbar{left:0;top:0;width:1200px;height:46px;background:var(--teal)}
.topbar .right{position:absolute;right:0;top:0;width:320px;height:46px;background:var(--blue)}
.topbar .info{position:absolute;left:110px;top:14px;color:var(--white);font-size:13px;display:flex;gap:14px;align-items:center}
.socials{display:flex;gap:8px}
.socials span{width:34px;height:34px;border:2px solid var(--white);border-radius:50%;display:block}
.topbar .socials{position:absolute;right:112px;top:6px}
/* nav */
.nav{left:0;top:46px;width:1200px;height:74px;background:var(--white)}
.brand{position:absolute;left:112px;top:18px;display:flex;align-items:center;gap:10px}
.brand i{width:34px;height:34px;border-radius:50%;background:var(--blue);display:block}
.brand b{font-family:"Montserrat",sans-serif;font-weight:600;font-size:14px;color:var(--blue);line-height:17px;width:170px}
.menu{position:absolute;right:110px;top:30px;display:flex;gap:28px;font-family:"Montserrat",sans-serif;font-weight:700;font-size:13px;color:var(--ink)}
/* hero */
.hero-photo{left:0;top:120px;width:1200px;height:760px;background:linear-gradient(110deg,#35591e 0%,#6f9a3e 45%,#c9d7c2 70%,#5a7f38 100%)}
.hero-title{left:110px;top:300px;color:var(--white);font-size:28px;line-height:42px;font-weight:700}
/* coaching */
.grey-band{left:0;top:720px;width:1200px;height:758px;background:var(--light)}
.section-title{width:1200px;text-align:center;font-size:22px;font-weight:700}
.card{position:absolute;top:910px;width:312px;height:395px;background:var(--white);border-radius:6px;box-shadow:0 2px 8px rgba(0,0,0,.15);text-align:center}
.card .photo{left:7px;top:7px;width:298px;height:195px}
.card h3{position:absolute;top:218px;left:0;width:100%;font-family:"Montserrat",sans-serif;font-size:14px;font-weight:600;color:var(--blue);line-height:24px;text-transform:uppercase}
.card p{position:absolute;top:272px;left:14px;width:284px;font-size:13px;line-height:22px;color:var(--grey)}
.more{position:absolute;left:0;width:100%;font-family:"Montserrat",sans-serif;font-weight:700;font-size:13px;color:var(--teal)}
.card .more{top:360px}
.arrow{position:absolute;top:1090px}
/* about */
.about-photo{left:128px;top:1578px;width:434px;height:434px;border-radius:50%;background:radial-gradient(circle at 40% 40%,#d6b48e,#7a9e4a 70%);border:8px solid var(--white)}
.about-text{left:640px;top:1612px;width:450px}
.about-text h2{font-family:"Montserrat",sans-serif;font-size:32px;font-weight:600;margin-bottom:26px}
.about-text p{font-size:13.5px;line-height:26px;color:#555;text-align:justify}
/* orgs */
.blue-band{left:0;top:2105px;width:1200px;height:543px;background:var(--blue)}
.org-photo{top:2235px;width:314px;height:205px}
.org-box{position:absolute;top:2415px;width:290px;height:172px;background:var(--white);border-radius:6px;text-align:center}
.org-box h3{margin-top:14px;font-family:"Montserrat",sans-serif;font-size:15px;font-weight:600;color:var(--blue);text-transform:uppercase}
.org-box p{margin:10px 12px 0;font-size:13px;line-height:22px;color:var(--grey)}
.org-box .more{top:136px}
/* features */
.frame{position:absolute;border-radius:8px}
.feat-photo{border:6px solid var(--white);box-shadow:0 2px 10px rgba(0,0,0,.2)}
.icon-circle{position:absolute;width:80px;height:80px;border-radius:50%;background:var(--white);box-shadow:0 2px 8px rgba(0,0,0,.15);display:flex;align-items:center;justify-content:center}
.feat h2{font-family:"Montserrat",sans-serif;font-size:22px;font-weight:600;line-height:32px;text-transform:uppercase}
.feat p{margin-top:20px;font-size:13.5px;line-height:26px;color:var(--grey)}
/* book */
.book-photo{left:0;top:3890px;width:1200px;height:410px;background:linear-gradient(180deg,#5e6e44 0%,#a3a07a 50%,#6f7f3c 100%)}
.book-box{left:180px;top:3650px;width:840px;height:315px;background:var(--teal);color:var(--white)}
.book-box h2{position:absolute;left:0;top:60px;width:600px;text-align:center;font-family:"Montserrat",sans-serif;font-size:25px;font-weight:700;line-height:34px}
.book-box p{position:absolute;left:0;top:142px;width:600px;text-align:center;font-size:16px;line-height:26px}
.book-cover{left:592px;top:25px;width:176px;height:270px;background:linear-gradient(180deg,#f4f4f4 0%,#e6e6e6 60%,#c0392b 100%);box-shadow:6px 6px 10px rgba(0,0,0,.3)}
/* staying ahead */
.ahead{left:190px;top:4435px;width:820px;height:146px;border:4px solid var(--teal);border-radius:6px}
.ahead h2{position:absolute;left:50%;top:-22px;transform:translateX(-50%);background:var(--white);padding:0 12px;font-family:"Montserrat",sans-serif;font-size:32px;font-weight:600;white-space:nowrap}
.ahead p{position:absolute;top:40px;left:0;width:100%;text-align:center;font-size:25px;line-height:38px;color:#666}
/* footer */
.footer{left:0;top:4840px;width:1200px;height:293px;background:var(--dark);color:var(--white);text-align:center}
.footer .brand{position:static;justify-content:center;margin-top:40px}
.footer .brand i{background:var(--white)}
.footer .brand b{color:var(--white);width:auto;font-size:15px}
.fmenu{margin-top:28px;display:flex;justify-content:center;gap:32px;font-family:"Montserrat",sans-serif;font-weight:700;font-size:14px}
.fcontact{margin-top:14px;font-size:15px}
.footer .socials{justify-content:center;margin-top:18px}
.footer .socials span{border-color:var(--teal)}
.copy{position:absolute;top:262px;width:100%;font-size:12px;color:#ccc}
</style>
</head>
<body>

<div class="abs topbar">
  <div class="right"></div>
  <div class="info"><span>✉ info@brevantmoor.example</span><span>|</span><span>⌖ 4410 Larkspur Ave Fairview IN 46000</span></div>
  <div class="socials"><span></span><span></span><span></span></div>
</div>

<header class="abs nav">
  <div class="brand"><i></i><b>Brevantmoor Center for Medical Assistance Canines</b></div>
  <nav class="menu"><span>THE CENTER ⌄</span><span>HELPING ORGANIZATIONS ⌄</span><span>TEACHING TRAINERS ⌄</span><span>RESEARCH</span><span>CONTACT</span></nav>
</header>

<div class="photo hero-photo" role="img" aria-label="Trainer outdoors on grass raising a hand as a white dog jumps toward it"></div>
<div class="abs grey-band"></div>
<svg class="abs" style="left:0;top:620px" width="1200" height="260" viewBox="0 0 1200 260">
  <path d="M0 260 L0 190 C150 60 330 40 520 80 C700 120 820 160 1000 110 C1100 80 1160 60 1200 45 L1200 260Z" fill="var(--blue)"/>
  <path d="M0 260 L0 220 C160 100 330 80 520 112 C700 140 820 170 1000 130 C1100 106 1160 90 1200 80 L1200 260Z" fill="var(--teal)"/>
  <path d="M0 260 L0 250 C160 130 330 110 520 135 C700 160 820 190 1000 155 C1100 135 1160 120 1200 110 L1200 260Z" fill="var(--light)"/>
</svg>
<h1 class="abs head hero-title">The Brevantmoor Center<br>for Medical Assistance Canines</h1>
<a class="btn teal" style="left:110px;top:408px;width:198px;height:48px">Online Coaching</a>
<a class="btn blue" style="left:318px;top:408px;width:198px;height:48px">In Person Coaching</a>

<h2 class="abs head section-title" style="top:836px">Coaching for Service Dog Professionals</h2>
<svg class="arrow" style="left:48px" width="20" height="30" viewBox="0 0 20 30"><path d="M16 3 L4 15 L16 27" stroke="var(--teal)" stroke-width="3" fill="none"/></svg>
<svg class="arrow" style="left:1132px" width="20" height="30" viewBox="0 0 20 30"><path d="M4 3 L16 15 L4 27" stroke="var(--teal)" stroke-width="3" fill="none"/></svg>

<article class="card" style="left:110px">
  <div class="photo" role="img" aria-label="Trainers walking dogs on leashes indoors" style="background:linear-gradient(135deg,#7d6a55,#cfc5b5)"></div>
  <h3>Full curriculum - all you need to<br>train a medical assistant dog</h3>
  <p>Learn everything you need to become a professional service dog trainer and specialize in medical alert dogs.</p>
  <span class="more">LEARN MORE ➜</span>
</article>
<article class="card" style="left:442px">
  <div class="photo" role="img" aria-label="Row of testing stations with a dog sitting in one" style="background:linear-gradient(135deg,#9aa0a4,#e1ddd2)"></div>
  <h3>Service dog candidate<br>selection</h3>
  <p>This course covers everything about dogs. You will have access to our temperament testing protocols</p>
  <span class="more">LEARN MORE ➜</span>
</article>
<article class="card" style="left:774px">
  <div class="photo" role="img" aria-label="Classroom of students facing a projected presentation" style="background:linear-gradient(135deg,#8a7a6a,#c8d4d8)"></div>
  <h3>Service dog training and<br>assessments</h3>
  <p>A solid service dog program requires standards, tracking, and testing protocols for the dogs in training.</p>
  <span class="more">LEARN MORE ➜</span>
</article>
<a class="btn teal" style="left:496px;top:1362px;width:208px;height:48px">View All Services</a>

<svg class="abs" style="left:108px;top:1566px" width="470" height="470" viewBox="0 0 470 470"><path d="M235 8 A227 227 0 0 0 235 462" stroke="var(--blue)" stroke-width="8" fill="none"/></svg>
<div class="photo about-photo" role="img" aria-label="Woman kneeling in a garden giving a hand signal to a seated beagle"></div>
<section class="abs about-text">
  <h2>ABOUT US</h2>
  <p>The Brevantmoor Center for Medical Assistance Canines (BCMAC) offers a variety of teaching and coaching services. Elena Marsh Ph.D. assists organizations in developing and implementing new service dog programs and teaches professional dog trainers about medical assistance dogs. When the situation allows, she offers in-person tailored consulting services based on the organization's needs or online options.</p>
</section>
<a class="btn teal" style="left:640px;top:1920px;width:150px;height:46px">Learn More</a>

<div class="abs blue-band"></div>
<h2 class="abs head section-title" style="top:2158px;color:var(--white);font-size:28px">Helping Organizations</h2>
<div class="photo org-photo" role="img" aria-label="Large group of trainers posing with their dogs" style="left:112px;background:linear-gradient(135deg,#3d4e6e,#9aa7b8)"></div>
<div class="photo org-photo" role="img" aria-label="Audience attending a seminar with a projected screen" style="left:443px;background:linear-gradient(135deg,#6a4a3e,#c9b8a8)"></div>
<div class="photo org-photo" role="img" aria-label="Service dog in a red vest looking out an airport window" style="left:774px;background:linear-gradient(135deg,#aab4b8,#e6e6e2)"></div>
<div class="org-box" style="left:124px"><h3>Program consulting</h3><p>Helping organizations get started, improve their training program, and add services</p><span class="more">LEARN MORE ➜</span></div>
<div class="org-box" style="left:455px"><h3>Presentations &amp; seminars</h3><p>Sharing knowledge about service dogs and medical detection.</p><span class="more">LEARN MORE ➜</span></div>
<div class="org-box" style="left:786px"><h3>International services</h3><p>Fluent in both English and French, in-person and online coaching around the world.</p><span class="more">LEARN MORE ➜</span></div>

<div class="frame" style="left:112px;top:2745px;width:446px;height:340px;border:6px solid var(--teal)"></div>
<div class="photo feat-photo" role="img" aria-label="Trainer working with a black dog on a leash indoors" style="left:134px;top:2768px;width:448px;height:340px;background:linear-gradient(135deg,#c9c4b8,#7a8aa0 60%,#3b3b3b)"></div>
<div class="icon-circle" style="left:645px;top:2775px"><svg width="40" height="40" viewBox="0 0 40 40" fill="none" stroke="var(--teal)" stroke-width="2"><circle cx="12" cy="8" r="3"/><path d="M12 12 V34 M8 20 H16 M22 34 V22 L30 18 L34 24 V34"/></svg></div>
<section class="abs feat" style="left:645px;top:2875px;width:450px">
  <h2>Professional coaching/<br>teaching for dog trainers</h2>
  <p>Helping dog trainers improve their skills and learn about service dog training and medical alert dog training.</p>
</section>
<a class="btn teal" style="left:645px;top:3035px;width:152px;height:47px">Learn More</a>

<div class="icon-circle" style="left:110px;top:3238px"><svg width="40" height="40" viewBox="0 0 40 40" fill="none" stroke="var(--blue)" stroke-width="2"><circle cx="14" cy="14" r="6"/><circle cx="24" cy="24" r="9"/><path d="M30 30 L36 36"/></svg></div>
<section class="abs feat" style="left:112px;top:3338px;width:450px">
  <h2>Collaborating in research<br>projects</h2>
  <p>Collaborating in research studies in the field of Medical Detection Dogs.</p>
</section>
<a class="btn teal" style="left:112px;top:3497px;width:150px;height:47px">Learn More</a>
<div class="frame" style="left:642px;top:3205px;width:448px;height:345px;border:6px solid var(--blue)"></div>
<div class="photo feat-photo" role="img" aria-label="Yellow labrador in a vest sniffing a scent can on a tiled floor" style="left:618px;top:3228px;width:444px;height:344px;background:linear-gradient(135deg,#d8d2c6,#b0a898 60%,#8a8a8a)"></div>

<div class="photo book-photo" role="img" aria-label="White labrador leaping toward a trainer in a park"></div>
<section class="abs book-box">
  <h2>NEW BOOK FROM ELENA<br>MARSH PH.D.!</h2>
  <p>Choosing And Raising Your Service Dog: A Guide<br>to Public Access Work</p>
  <a class="btn" style="left:224px;top:238px;width:152px;height:48px;background:var(--white);color:var(--teal)">Order Now</a>
  <div class="photo book-cover" role="img" aria-label="Book cover with a service dog in a red vest"></div>
</section>

<div class="abs ahead">
  <h2>STAYING AHEAD</h2>
  <p>Science-based and ethical training methods for the<br>modern service dog trainer</p>
</div>
<a class="btn teal" style="left:525px;top:4576px;width:150px;height:46px">Get Started</a>

<svg class="abs" style="left:0;top:4700px" width="1200" height="150" viewBox="0 0 1200 150">
  <path d="M0 150 L0 110 C200 20 380 30 560 80 C760 130 960 60 1200 0 L1200 150Z" fill="var(--blue)"/>
  <path d="M0 150 L0 130 C200 50 380 60 560 105 C760 150 960 90 1200 35 L1200 150Z" fill="var(--teal)"/>
  <path d="M0 150 L0 145 C200 80 380 85 560 125 C760 165 960 115 1200 70 L1200 150Z" fill="var(--dark)"/>
</svg>
<footer class="abs footer">
  <div class="brand"><i></i><b>Brevantmoor Center for Medical Assistance Canines</b></div>
  <nav class="fmenu"><span>THE CENTER</span><span>HELPING ORGANIZATIONS</span><span>TEACHING TRAINERS</span><span>RESEARCH</span><span>CONTACT</span></nav>
  <p class="fcontact">✉ info@brevantmoor.example &nbsp;|&nbsp; ⌖ 4410 Larkspur Ave Fairview IN 46000</p>
  <div class="socials"><span></span><span></span><span></span></div>
  <p class="copy">© 2021 Company Name. All Rights Reserved</p>
</footer>

</body>
</html>
```